Birth Announcement ... drawing that can be framed

My daughter ( Dana ) and her husband ( Colm ) are expecting the birth
of their first child (boy) in September and I would like to do a cartoon
illustration announcing the event to all the family and friends. Something
colorful, vibrant, playful, showing movement.
Some of the basic facts I would like to draw from :
Colm is Irish and works at Quillmark
Dana is half Irish and works at Harbrook (accounting company)
They have a Scottish Terrier (greyish black color) who is their current baby. We are all going to the Brindlewood Stakes  and taking a Oakbarrel Route tour in May.
I was thinking of a couple scenarios (but I am open to your input)
First scenario ... Mom and Dad are at the Stakes standing at the finish line
The jockeys are all babies in different colored diapers Their baby is leading the race as he crosses the finish line .Their dog is holding a
winners cup with Bourbon written on it & says .. It's a boy !!!
Second scenario ... Mom and Dad are standing beside a " Stakes "
carousel with babies on the multi-colored wooden horses.Their dog
( toby) jumps up a pulls one off a horse by his diaper. Mom and Dad are calling out ...It' a boy !!!
Please call my toll free work number 888-555-0147 or E-mail
gil@marrowpostrail.example at you have any questions.
Thanks,
Gil Falkner

Reason: Not quite satisfied with any of the designs to date.  Please use attached images as a guideline.  Thank you.

```html
<!DOCTYPE html>
<html lang="en">
<head>
<meta charset="utf-8">
<title>Baby on the Way – Colm and Dana</title>
<link rel="stylesheet" href="https://fonts.googleapis.com/css2?family=Dancing+Script:wght@700&family=Roboto:wght@700&display=swap">
<style>
  :root {
    --backdrop: #f2f0ed;
    --poster-pink: #e5137a;
    --sun-yellow: #f7b924;
    --text-white: #ffffff;
    --dog-grey: #2f2f33;
    --pillow-blue: #a9d8ef;
  }
  html, body {
    margin: 0;
    width: 1200px;
    height: 1200px;
    overflow: hidden;
    background: var(--backdrop);
  }
  .poster {
    position: absolute;
    left: 202px;
    top: 40px;
    width: 796px;
    height: 1120px;
    background: var(--poster-pink);
    overflow: hidden;
  }
  .poster-art {
    position: absolute;
    inset: 0;
  }
  .headline {
    position: absolute;
    left: 0;
    width: 100%;
    text-align: center;
    font-family: "Dancing Script", cursive;
    font-weight: 700;
    color: var(--text-white);
    margin: 0;
    line-height: 1;
  }
  .headline-baby { top: 462px; font-size: 140px; padding-left: 10px; }
  .headline-on-the { top: 612px; font-size: 50px; padding-left: 28px; }
  .headline-way { top: 680px; font-size: 140px; padding-left: 10px; }
  .parents {
    position: absolute;
    left: 62px;
    top: 908px;
    margin: 0;
    font-family: "Roboto", sans-serif;
    font-weight: 700;
    font-size: 48px;
    color: var(--sun-yellow);
    line-height: 1;
  }
  .announcement {
    position: absolute;
    left: 62px;
    top: 990px;
    margin: 0;
    font-family: "Dancing Script", cursive;
    font-weight: 700;
    font-size: 40px;
    color: var(--text-white);
    line-height: 1;
  }
</style>
</head>
<body>
  <main class="poster">
    <svg class="poster-art" width="796" height="1120" viewBox="0 0 796 1120">
      <g class="confetti-dots" fill="var(--sun-yellow)">
        <circle cx="162" cy="95" r="9"/>
        <circle cx="338" cy="63" r="6"/>
        <circle cx="524" cy="130" r="9"/>
        <circle cx="705" cy="192" r="6"/>
        <circle cx="155" cy="235" r="6"/>
        <circle cx="136" cy="433" r="6"/>
      </g>
      <circle class="sun-disc" cx="399" cy="249" r="119" fill="var(--sun-yellow)"/>
      <rect class="dog-photo" x="212" y="160" width="330" height="515" rx="60"
            fill="var(--dog-grey)" role="img"
            aria-label="Photo of a greyish black Scottish Terrier puppy sitting and facing forward"/>
      <rect class="baby-pillow" x="547" y="918" width="95" height="150" rx="18"
            fill="var(--pillow-blue)" role="img"
            aria-label="Illustration of a baby in blue sitting on a dotted blue pillow"/>
      <g class="paw-icon" fill="none" stroke="var(--text-white)" stroke-width="3">
        <g transform="translate(520 985)">
          <ellipse cx="0" cy="8" rx="11" ry="9"/>
          <circle cx="-13" cy="-6" r="4"/>
          <circle cx="-5" cy="-13" r="4"/>
          <circle cx="5" cy="-13" r="4"/>
          <circle cx="13" cy="-6" r="4"/>
        </g>
        <g transform="translate(737 1025)">
          <ellipse cx="0" cy="8" rx="11" ry="9"/>
          <circle cx="-13" cy="-6" r="4"/>
          <circle cx="-5" cy="-13" r="4"/>
          <circle cx="5" cy="-13" r="4"/>
          <circle cx="13" cy="-6" r="4"/>
        </g>
      </g>
    </svg>

    <h1 class="headline headline-baby">Baby</h1>
    <p class="headline headline-on-the">on the</p>
    <p class="headline headline-way">Way</p>

    <p class="parents">Colm and Dana</p>
    <p class="announcement">are having a baby boy!</p>
  </main>
</body>
</html>
```